Lindenfall Studio Business cards

Design our business cards and eventually a logo. The company is based in Paris, its activity is the retailing via internet of luxury home furniture (like Vantorelli, Bercasso, fradusi...) Our clients are international andwith a high sense of aesthetics. The design shall communicate wealth and trust with a high quality and aesthetic sense, pure lines Company Name is Lindenfall StudioExplanation of the name: usually people who wants to buy furniture usually go in a showroom. Today they go in showroom to test the furniture and they search for the price on internet, which is a "Lindenfall studio".We will not be a e-commerce site. Our site will be (another project) a presentation site which purpose is to reach qualified prospects. Then everything will be handled by phone, meeting etc.The business card must be professional as we will negotiate with many luxury brands, opportunity to represent them on our site, prices etc.As far as the color are concerned mostly black and whithe or grey. The font of the Lindenfall Studio name shall have some impact.

Target Market(s)

High-end furniture and buyers of luxury goods, international customers, mostly women who handle such projects.
We also deal with professional buyers (hotels as an example) and luxury brands

Contact Information for Business Card

standard format 85x55, lanscape card, square corners will be printed on thick high quality paper (300 or 350g)

Font styles to use
Sans Serif

Colors

Designer to choose colors to be used in the design.

Requirements
Must have
• Must be white, as the paper will be high quality, the paper will enhance the card.
• Name of the brand Lindenfall studio (with specific font which make it very nice looking and catch the attention. similar to Calibri or Calibri
• Name of person (will give you the name later (4 names and position)
• the position of the person
• Mobile phone, e-mail, Physical address 27, rue Caldenois, 75005 Paris, France (courrier only) our web site www.lindenfallstudio-example.fr
• The card must be simple and class
Nice to have
• Font of the address is smaller than the rest,
• Calibri font or similar on recto side with the name of the company which may look similar to the picture inserted in the brief.
• The grey color in the picture inserted is ok for us
Should not have
• Any parallel lines which represent the name of the company
• Any heavy design If you go on internet sites which present the furniture all designs are pure lines and high quality craftsmanship. To have an idea of our targetted client or brand we will be in touch: https://www.casavornetta-example.it/projects/
• Note that the picture added below is what we use, now as mail signature, up to you to have a better design etc.

```html
<!DOCTYPE html>
<html lang="fr">
<head>
<meta charset="utf-8">
<title>Lindenfall Studio — Business Card</title>
<link href="https://fonts.googleapis.com/css2?family=Carlito:wght@400;700&display=swap" rel="stylesheet">
<style>
  :root {
    --page-bg: #e4e4e4;
    --card-white: #ffffff;
    --ink: #23262d;
    --ink-soft: #5b5f68;
    --gold: #c9b288;
    --gold-light: #efe1c2;
    --gold-dark: #9a815b;
  }
  html, body {
    margin: 0;
    width: 1200px;
    height: 1000px;
    overflow: hidden;
    background: var(--page-bg);
  }
  .business-card {
    position: absolute;
    left: 120px;
    top: 190px;
    width: 960px;
    height: 621px;
    background: var(--card-white);
    box-shadow: 0 18px 40px rgba(0,0,0,0.18);
    overflow: hidden;
    font-family: "Carlito", "Calibri", sans-serif;
    color: var(--ink);
  }
  .card-ornaments {
    position: absolute;
    inset: 0;
    width: 960px;
    height: 621px;
  }
  .company-name {
    position: absolute;
    right: 92px;
    top: 92px;
    margin: 0;
    font-size: 40px;
    font-weight: 700;
    letter-spacing: 0.5px;
    color: var(--ink);
  }
  .person {
    position: absolute;
    left: 114px;
    top: 352px;
  }
  .person-name {
    margin: 0;
    font-size: 31px;
    font-weight: 700;
    line-height: 1;
    color: var(--ink);
  }
  .person-role {
    margin: 6px 0 0;
    font-size: 17px;
    color: var(--ink-soft);
  }
  .contact-list {
    position: absolute;
    left: 118px;
    top: 432px;
    margin: 0;
    padding: 0;
    list-style: none;
    font-size: 18px;
    color: var(--ink-soft);
  }
  .contact-item {
    display: flex;
    align-items: center;
    gap: 16px;
    height: 34px;
  }
  .contact-icon { width: 18px; height: 18px; flex: none; }
  .address {
    position: absolute;
    right: 92px;
    top: 462px;
    margin: 0;
    font-size: 15px;
    line-height: 1.4;
    text-align: right;
    font-style: normal;
    color: var(--ink-soft);
  }
</style>
</head>
<body>
  <section class="business-card">
    <svg class="card-ornaments" viewBox="0 0 960 621" aria-hidden="true">
      <defs>
        <linearGradient id="gold-sheen" x1="0" y1="0" x2="1" y2="1">
          <stop offset="0" stop-color="#9a815b"/>
          <stop offset="0.45" stop-color="#efe1c2"/>
          <stop offset="1" stop-color="#a88e66"/>
        </linearGradient>
      </defs>
      <polygon class="edge-tab-left" fill="url(#gold-sheen)"
               points="0,200 44,214 66,246 66,388 44,420 0,432"/>
      <polygon class="edge-tab-right" fill="url(#gold-sheen)"
               points="960,226 916,240 894,272 894,414 916,446 960,458"/>
    </svg>

    <h1 class="company-name">LINDENFALL STUDIO SAS</h1>

    <div class="person">
      <p class="person-name">Élodie Marchetti</p>
      <p class="person-role">Présidente &amp; Co-Founder</p>
    </div>

    <ul class="contact-list">
      <li class="contact-item">
        <svg class="contact-icon" viewBox="0 0 24 24" aria-hidden="true">
          <path fill="#9a815b" d="M6.6 10.8a15.5 15.5 0 0 0 6.6 6.6l2.2-2.2c.3-.3.7-.4 1-.2 1.1.4 2.3.6 3.6.6.6 0 1 .4 1 1V20c0 .6-.4 1-1 1A17 17 0 0 1 3 4c0-.6.4-1 1-1h3.5c.6 0 1 .4 1 1 0 1.3.2 2.5.6 3.6.1.3 0 .7-.2 1z"/>
        </svg>
        <span>+33614729305</span>
      </li>
      <li class="contact-item">
        <svg class="contact-icon" viewBox="0 0 24 24" aria-hidden="true">
          <rect x="2" y="5" width="20" height="14" rx="1.5" fill="#9a815b"/>
          <path d="M3 6.5l9 6.5 9-6.5" fill="none" stroke="#ffffff" stroke-width="1.4"/>
        </svg>
        <span>contact@lindenfallstudio-example.fr</span>
      </li>
      <li class="contact-item">
        <svg class="contact-icon" viewBox="0 0 24 24" aria-hidden="true">
          <circle cx="12" cy="12" r="10" fill="#9a815b"/>
          <g fill="none" stroke="#ffffff" stroke-width="1.3">
            <ellipse cx="12" cy="12" rx="4.5" ry="10"/>
            <line x1="2" y1="12" x2="22" y2="12"/>
          </g>
        </svg>
        <span>www.lindenfallstudio-example.fr</span>
      </li>
    </ul>

    <address class="address">27 rue Caldenois<br>75005 Paris, France</address>
  </section>
</body>
</html>
```